Artist needs a business card for her pencil portraits and streetscapes

My mum is an artist and does fabulous portraits and sketches with pencil and needs a business card.
She likes designs that are a bit weird or unusual. The winning design will NOT be a slick modern corporate looking logo. It should be a little bit rustic and different. Interesting patterns and textures would be great, it doesn't even need to look like a business card! Come up with something unique!

Target Market(s)

Older clientele looking for family portraits

Industry/Entity Type

Artists

Contact Information for Business Card

Basically just need the name and contact details

Font styles to use
Decorative
Script

Requirements
Must have
• Lena Dorsby
• Artist
• 0427193662
• lenadorsby@postvale.com
Nice to have
• Weird artistic backgrounds, interesting textures, unusual designs for an artistic woman.
Should not have
• Nothing ultra modern and nothing corporate looking.

```html
<!DOCTYPE html>
<html lang="en">
<head>
<meta charset="utf-8">
<title>Lena Dorsby – Artist Business Card</title>
<link href="https://fonts.googleapis.com/css2?family=Patrick+Hand&display=swap" rel="stylesheet">
<style>
  :root {
    --backdrop-inner: #4a4a4a;
    --backdrop-outer: #161616;
    --wood-light: #e2b888;
    --wood-mid: #c9946a;
    --wood-warm: #d9a066;
    --wood-dark: #a9785a;
    --ink-carved: #6a4630;
    --ink-highlight: rgba(255, 236, 210, 0.55);
  }
  * { margin: 0; padding: 0; box-sizing: border-box; }
  html, body {
    width: 1200px;
    height: 1200px;
    overflow: hidden;
  }
  body {
    background: radial-gradient(circle at 50% 45%, var(--backdrop-inner) 0%, var(--backdrop-outer) 85%);
    display: flex;
    align-items: center;
    justify-content: center;
    font-family: "Patrick Hand", cursive;
  }
  .business-card {
    position: relative;
    width: 1050px;
    height: 600px;
    border-radius: 34px;
    overflow: hidden;
    box-shadow: 0 24px 50px rgba(0, 0, 0, 0.55);
  }
  .wood-texture {
    position: absolute;
    inset: 0;
    background:
      linear-gradient(180deg, rgba(255,255,255,0.06) 0%, rgba(0,0,0,0.04) 33%, rgba(255,255,255,0.08) 34%, rgba(0,0,0,0.05) 66%, rgba(255,255,255,0.07) 67%, rgba(0,0,0,0.06) 100%),
      linear-gradient(100deg, var(--wood-dark) 0%, var(--wood-mid) 25%, var(--wood-light) 55%, var(--wood-warm) 80%, var(--wood-mid) 100%);
  }
  .card-content {
    position: absolute;
    inset: 0;
    color: var(--ink-carved);
    text-shadow: 1px 1px 0 var(--ink-highlight), -1px -1px 1px rgba(60, 35, 20, 0.35);
  }
  .artist-name {
    position: absolute;
    left: 300px;
    top: 150px;
    font-size: 104px;
    font-weight: 400;
    line-height: 1;
    letter-spacing: 2px;
  }
  .artist-role {
    position: absolute;
    left: 500px;
    top: 262px;
    font-size: 62px;
    line-height: 1;
    letter-spacing: 2px;
  }
  .contact-line {
    position: absolute;
    display: flex;
    align-items: center;
    gap: 14px;
    font-size: 50px;
    line-height: 1;
    letter-spacing: 2px;
  }
  .contact-phone { left: 440px; top: 352px; }
  .contact-email { left: 340px; top: 440px; }
  .contact-icon {
    width: 34px;
    height: 28px;
    fill: none;
    stroke: var(--ink-carved);
    stroke-width: 3;
    stroke-linejoin: round;
    flex-shrink: 0;
  }
</style>
</head>
<body>
  <article class="business-card">
    <div class="wood-texture" role="img" aria-label="Warm light wood plank texture background"></div>
    <div class="card-content">
      <h1 class="artist-name">Lena Dorsby</h1>
      <p class="artist-role">Artist</p>
      <p class="contact-line contact-phone">
        <svg class="contact-icon" viewBox="0 0 34 28" aria-hidden="true">
          <path d="M3 10 Q17 0 31 10 L27 13 L23 9 L11 9 L7 13 Z"/>
          <path d="M9 14 L25 14 L28 25 L6 25 Z"/>
          <circle cx="17" cy="19.5" r="3"/>
        </svg>
        <span>0427193662</span>
      </p>
      <p class="contact-line contact-email">
        <svg class="contact-icon" viewBox="0 0 34 28" aria-hidden="true">
          <rect x="3" y="5" width="28" height="19"/>
          <path d="M3 5 L17 16 L31 5"/>
        </svg>
        <span>lenadorsby@postvale.com</span>
      </p>
    </div>
  </article>
</body>
</html>
```